Business Card Design.

Life and Wellness Coach
www.brightpathwell.net
Want to use my name as the logo it could be the initials TRK or my full name. I want to trade mark me.
I like clean lines and simple designs, but it pops using the colors scheme (one or two colors) on the website.
I provide life and health coaching virtually and in person. My services include: Dietary Signal Screening, Sensitivity Clearing Review, Wellness Coaching, Life Coaching. Life and Health Assessments, and I sell foundational health products and specialized nutrition. Use colors that represent healing and trust.
Target Market(s)
Women for the ages of 30 - 60
Industry/Entity Type
Health
Contact Information for Business Card
Tessa Rosalind Kimble
Life and Wellness Coach
tessa@coachtrk.net
www.brightpathwell.net
555-217-8364
Health is not an event it's a lifestyle (tag line or if you have a better tag line)

```html
<!DOCTYPE html>
<html lang="en">
<head>
<meta charset="utf-8">
<title>Tessa Rosalind Kimble — Business Card</title>
<link rel="stylesheet" href="https://fonts.googleapis.com/css2?family=Open+Sans:ital,wght@0,300;0,400;1,300&display=swap">
<style>
  :root {
    --stage: #e9e6e1;
    --card-light: #6d6d6d;
    --card-dark: #3a3a3a;
    --ink: #ffffff;
    --ink-soft: #e4e4e4;
    --band: #f4f4f4;
    --photo-warm: #8a5a44;
    --photo-blue: #4b43a8;
  }
  * { box-sizing: border-box; margin: 0; padding: 0; }
  html, body { width: 1200px; height: 900px; overflow: hidden; }
  body {
    background: var(--stage);
    font-family: "Open Sans", Arial, sans-serif;
    color: var(--ink);
    display: flex;
    align-items: center;
    justify-content: center;
    gap: 50px;
  }
  .card {
    position: relative;
    width: 525px;
    height: 300px;
    border-radius: 4px;
    overflow: hidden;
    background: linear-gradient(135deg, var(--card-light) 0%, var(--card-dark) 100%);
    box-shadow: 0 10px 28px rgba(0,0,0,.25);
  }
  .card-art { position: absolute; inset: 0; width: 100%; height: 100%; }
  .wordmark {
    position: absolute;
    font-weight: 300;
    letter-spacing: .12em;
    color: var(--ink);
    line-height: 1;
  }
  .card-front .wordmark { top: 30px; left: 296px; font-size: 50px; }
  .identity { position: absolute; left: 296px; top: 112px; width: 215px; }
  .identity-name { font-size: 20px; font-weight: 400; line-height: 1.2; white-space: nowrap; }
  .identity-role { font-size: 12px; font-weight: 300; color: var(--ink-soft); margin-top: 3px; }
  .identity-rule { height: 1px; background: var(--ink-soft); margin: 10px 0 8px; width: 200px; }
  .contact-list { list-style: none; font-size: 12.5px; font-weight: 300; line-height: 1.75; color: var(--ink-soft); }
  .card-back .wordmark {
    top: 50%; left: 50%;
    transform: translate(-50%, -58%);
    font-size: 96px;
  }
  .tagline {
    position: absolute;
    left: 26px; bottom: 24px;
    font-size: 13px;
    font-style: italic;
    font-weight: 300;
    color: var(--ink-soft);
  }
</style>
</head>
<body>
  <section class="card card-front" aria-label="Card front">
    <svg class="card-art" viewBox="0 0 525 300" preserveAspectRatio="none">
      <defs>
        <linearGradient id="portrait-tone" x1="0" y1="0" x2="1" y2="1">
          <stop offset="0" stop-color="#5a3426"/>
          <stop offset=".55" stop-color="var(--photo-warm)"/>
          <stop offset="1" stop-color="var(--photo-blue)"/>
        </linearGradient>
      </defs>
      <path class="curve-band" d="M0 52 Q140 50 205 120 Q252 180 262 300 L0 300 Z" fill="var(--band)"/>
      <path class="portrait-area" role="img" aria-label="Portrait photograph of the coach" d="M0 80 Q125 80 185 134 Q230 186 240 300 L0 300 Z" fill="url(#portrait-tone)"/>
      <path class="curve-line" d="M0 42 Q155 40 222 115 Q270 178 280 300" fill="none" stroke="var(--band)" stroke-width="2.5"/>
    </svg>
    <div class="wordmark">TRK</div>
    <div class="identity">
      <h1 class="identity-name">Tessa Rosalind Kimble</h1>
      <p class="identity-role">Life and Wellness Coach</p>
      <div class="identity-rule"></div>
      <ul class="contact-list">
        <li>555-217-8364</li>
        <li>tessa@coachtrk.net</li>
        <li>www.brightpathwell.net</li>
      </ul>
    </div>
  </section>

  <section class="card card-back" aria-label="Card back">
    <div class="wordmark">TRK</div>
    <p class="tagline">Health is not an event it's a lifestyle</p>
  </section>
</body>
</html>
```